Etiketten-Design für Gin
Zielgruppe
Herstellung von Spirituosen/ Molk UG (haftungsbeschränkt)
Zielgruppe: Vorwiegend Männer von 45 bis 70 Jahre
Aufgabenstellung
Flaschen Etikett Vorder- und Rückseite für Gin
Wortmarke: Dry Gin Molk sollte hervorgehoben sein.
Bedeutung hat für uns auch, dass er aus der Region Rhein-Main kommt.

```html
<!DOCTYPE html>
<html lang="de">
<head>
<meta charset="utf-8">
<title>Dry Gin Molk – Etikett</title>
<link rel="stylesheet" href="https://fonts.googleapis.com/css2?family=Alfa+Slab+One&family=Archivo+Black&family=Oswald:wght@500&family=Smokum&display=swap">
<style>
  :root {
    --backdrop: #e9e8e5;
    --paper: #f5e7cd;
    --frame-gold: #c8954a;
    --ornament-gold: #d3a560;
    --brown: #6e4a2a;
    --scene-light: #fffaf0;
    --scene-tan: #c9955e;
    --red-bright: #e32b32;
    --red-deep: #8e1f25;
    --cream: #f6ead2;
    --ink: #333131;
  }
  html, body {
    margin: 0;
    width: 1200px;
    height: 1175px;
    overflow: hidden;
    background: var(--backdrop);
  }
  .label {
    position: absolute;
    left: 200px;
    top: 63px;
    width: 800px;
    height: 1049px;
    display: block;
  }
  .label-paper { fill: var(--paper); }
  .label-frame { fill: none; stroke: var(--frame-gold); stroke-width: 2; }
  .distillery-name {
    font-family: "Archivo Black", sans-serif;
    font-size: 50px;
    fill: var(--brown);
    letter-spacing: 1px;
  }
  .product-type {
    font-family: "Smokum", serif;
    font-size: 300px;
    fill: var(--cream);
    stroke: var(--red-deep);
    stroke-width: 3;
    paint-order: stroke;
  }
  .brand-word {
    font-family: "Alfa Slab One", serif;
    font-size: 220px;
    fill: var(--ink);
  }
  .brand-rule { stroke: var(--frame-gold); stroke-width: 3; }
  .process-note {
    font-family: "Oswald", sans-serif;
    font-weight: 500;
    font-size: 46px;
    fill: var(--ink);
  }
</style>
</head>
<body>
<svg class="label" viewBox="0 0 955 1252" xmlns="http://www.w3.org/2000/svg">
  <defs>
    <radialGradient id="scene-tone" cx="0.5" cy="0.3" r="0.7">
      <stop offset="0" stop-color="var(--scene-light)"/>
      <stop offset="0.55" stop-color="#e8c594"/>
      <stop offset="1" stop-color="var(--scene-tan)" stop-opacity="0.35"/>
    </radialGradient>
    <radialGradient id="banner-tone" cx="0.45" cy="0.5" r="0.6">
      <stop offset="0" stop-color="var(--red-bright)"/>
      <stop offset="1" stop-color="var(--red-deep)"/>
    </radialGradient>
    <linearGradient id="ornament-tone" x1="0" y1="0" x2="1" y2="0">
      <stop offset="0" stop-color="var(--ornament-gold)" stop-opacity="0"/>
      <stop offset="0.5" stop-color="var(--ornament-gold)" stop-opacity="0.35"/>
      <stop offset="1" stop-color="var(--ornament-gold)" stop-opacity="0"/>
    </linearGradient>
    <path id="distillery-arc" d="M200 205 Q477 110 754 205"/>
  </defs>

  <rect class="label-paper" x="0" y="0" width="955" height="1252"/>
  <rect class="label-frame" x="44" y="40" width="864" height="1168"/>

  <rect class="top-ornament" x="92" y="62" width="735" height="80" fill="url(#ornament-tone)" role="img" aria-label="Geschwungene Zierranken oben"/>

  <text class="distillery-name" text-anchor="middle">
    <textPath href="#distillery-arc" startOffset="50%">DESTILLERIE MOLK</textPath>
  </text>

  <ellipse class="landscape" cx="467" cy="395" rx="330" ry="205" fill="url(#scene-tone)" role="img" aria-label="Landschaft mit Fachwerkhaus, Bäumen und Sonnenstrahlen"/>

  <rect class="bottom-ornament" x="87" y="830" width="770" height="380" fill="url(#ornament-tone)" role="img" aria-label="Geschwungene Zierranken um die Wortmarke"/>

  <polygon class="banner" points="132,592 802,482 802,767 132,877" fill="url(#banner-tone)"/>

  <g transform="translate(467 752) rotate(-9.3)">
    <text class="product-type" x="0" y="0" text-anchor="middle" textLength="600" lengthAdjust="spacingAndGlyphs">DRY GIN</text>
  </g>

  <g transform="translate(477 977) rotate(-9.3)">
    <text class="brand-word" x="0" y="0" text-anchor="middle" textLength="600" lengthAdjust="spacingAndGlyphs">MOLK</text>
    <line class="brand-rule" x1="-300" y1="22" x2="320" y2="22"/>
  </g>

  <text class="process-note" x="297" y="1172" textLength="515" lengthAdjust="spacingAndGlyphs">2-fach destilliert im Kupferkessel</text>
</svg>
</body>
</html>
```